Business Card for new Overseas Property Buying Business

Hi

We need a new business card for our new business.

We are Faraway Nest Finders. So we search locations on behalf of our clients to find them the ideal home.

These are mainly holiday homes in nice locations - but sometimes people are looking to relocate.

I am looking for a nice simple design - that has some class and professionalism about it. Taking inspiration from our logo.

Text wise I was thinking of maybe having something like. (THE FONT FOR THIS SHOULD BE LIKE THE WRITING IN THE ATTACHMENT WITH THE MAP ON IT)

1)
What does your dream house have (tick all that apply):
swimming pool x
private vineyard x
herb garden x
full sized football pitch x

2)
How to buy a home abroad:

Method 1:
1) Scour internet for suitable estate agents
2) Arrange hectic holiday timetable with multiple agents in multiple languages
3) Fly to destination to find property was not as it seemed
4) Feel frustrated and helpless
OR
Method 2:
Contact your expert home hunter (details overleaf) - and leave the hard work to them

The end result should give people confidence that they are dealing with a professional organisation - and feel like they can place their trust in them. I would want it to drive them to either contact us directly or visit the website.

Please include name (Gordon Tramley), position (founder), contact numbers x 2, email address, website (www.quelvatrix-moor.com)

I look forward to seeing your entries.

Reason: Hi Sorry to extend - Xmas has got in the way of my plans. I will be providing feedback. Happy Christmas to you all.

```html
<!DOCTYPE html>
<html lang="en">
<head>
<meta charset="utf-8">
<title>Faraway Nest Finders – Business Card</title>
<link rel="stylesheet" href="https://fonts.googleapis.com/css2?family=Alfa+Slab+One&family=Arvo:wght@700&family=Delius&family=Reenie+Beanie&display=swap">
<style>
  :root {
    --canvas: #ececec;
    --frame: #4b4540;
    --map-light: #efe3c6;
    --map-warm: #e6c99c;
    --map-rose: #d9a08a;
    --paper: #ffffff;
    --ink: #1d1b1a;
    --brand-ink: #5a4a3e;
    --accent: #f0663a;
    --ring: #e2572c;
    --band-fog: rgba(255,255,255,0.55);
  }
  * { box-sizing: border-box; margin: 0; padding: 0; }
  html, body { width: 1200px; height: 1200px; overflow: hidden; }
  body {
    background: var(--canvas);
    display: flex;
    align-items: center;
    justify-content: center;
    gap: 28px;
  }
  .card {
    width: 546px;
    height: 322px;
    position: relative;
    overflow: hidden;
    box-shadow: 0 2px 6px rgba(0,0,0,0.18);
  }

  /* Front */
  .card--front { background: var(--frame); }
  .front__map {
    position: absolute;
    inset: 12px 10px 14px 10px;
    border-radius: 6px;
    background:
      radial-gradient(ellipse at 60% 40%, rgba(217,160,138,0.55), transparent 55%),
      radial-gradient(ellipse at 25% 30%, rgba(230,201,156,0.8), transparent 60%),
      linear-gradient(160deg, var(--map-light), var(--map-warm));
  }
  .front__band {
    position: absolute;
    left: 10px; right: 10px;
    top: 202px; height: 106px;
    background: var(--band-fog);
  }
  .front__name {
    position: absolute;
    top: 24px; right: 30px;
    text-align: right;
  }
  .front__person {
    font-family: "Alfa Slab One", serif;
    font-size: 27px;
    color: #fff;
    -webkit-text-stroke: 1.2px var(--ink);
    line-height: 1;
  }
  .front__role {
    font-family: "Arvo", serif;
    font-weight: 700;
    font-size: 19px;
    color: var(--ink);
    letter-spacing: 1.5px;
  }
  .brand {
    display: flex;
    align-items: center;
    gap: 8px;
    font-family: "Arvo", serif;
    font-weight: 700;
    color: var(--brand-ink);
  }
  .brand__dot {
    border-radius: 50%;
    background: var(--ring);
    flex: none;
  }
  .front__brand { position: absolute; top: 28px; left: 38px; font-size: 17px; }
  .front__brand .brand__dot { width: 40px; height: 40px; }
  .front__tagline {
    position: absolute;
    left: 70px; top: 140px;
    font-family: "Reenie Beanie", cursive;
    font-size: 40px;
    color: var(--ink);
  }
  .contact {
    position: absolute;
    left: 46px; top: 218px;
    list-style: none;
    font-family: "Arvo", serif;
    font-weight: 700;
    font-size: 16px;
    color: var(--ink);
  }
  .contact li { display: flex; align-items: center; gap: 10px; height: 25px; white-space: nowrap; }
  .contact svg { width: 15px; height: 15px; flex: none; }

  /* Back */
  .card--back { background: var(--paper); }
  .back__rule {
    position: absolute;
    left: 0; top: 0; bottom: 0;
    width: 10px;
    background: var(--accent);
  }
  .back__copy {
    position: absolute;
    left: 32px; top: 32px; right: 20px;
    font-family: "Delius", cursive;
    font-size: 11.5px;
    line-height: 1.3;
    color: var(--ink);
    font-style: italic;
  }
  .back__heading { color: var(--accent); margin-bottom: 18px; }
  .back__heading--gap { margin-top: 36px; margin-bottom: 14px; }
  .back__muted { color: #777; }
  .back__brand {
    position: absolute;
    right: 30px; top: 40px;
    flex-direction: column;
    gap: 8px;
    font-family: "Arvo", serif;
    text-align: center;
  }
  .back__brand .brand__dot { width: 70px; height: 70px; }
  .back__brand-name { font-size: 22px; line-height: 1.1; }
  .back__brand-sub { font-size: 10px; letter-spacing: 0.5px; }
</style>
</head>
<body>

<section class="card card--front" aria-label="Card front">
  <div class="front__map" role="img" aria-label="Torn-edged vintage world map in cream, tan and rose tones"></div>
  <div class="front__band"></div>

  <div class="brand front__brand">
    <span class="brand__dot"></span>
    <span>Quelvatrix Moor</span>
  </div>

  <div class="front__name">
    <p class="front__person">Gordon Tramley</p>
    <p class="front__role">founder</p>
  </div>

  <p class="front__tagline">you should be here with me</p>

  <ul class="contact">
    <li>
      <svg viewBox="0 0 16 16"><rect x="0.5" y="0.5" width="15" height="15" rx="3" fill="#1d1b1a"/><path d="M5 3.5c-1 .5-1.5 1.5-1 3 .8 2.5 3 4.8 5.5 5.6 1.3.4 2.3 0 2.8-1l-1.8-1.5-1.2.8c-1.2-.6-2.2-1.6-2.8-2.8l.8-1.2z" fill="#fff"/></svg>
      07700 900318 / 07700 900742
    </li>
    <li>
      <svg viewBox="0 0 16 16"><rect x="1" y="3" width="14" height="10" fill="none" stroke="#1d1b1a" stroke-width="1.3"/><path d="M1 3l7 6 7-6M1 13l5-5M15 13l-5-5" fill="none" stroke="#1d1b1a" stroke-width="1.1"/></svg>
      hello@quelvatrix-moor.com
    </li>
    <li>
      <svg viewBox="0 0 16 16"><circle cx="8" cy="8" r="6.8" fill="none" stroke="#1d1b1a" stroke-width="1.3"/><ellipse cx="8" cy="8" rx="3" ry="6.8" fill="none" stroke="#1d1b1a" stroke-width="1.1"/><path d="M1.2 8h13.6" stroke="#1d1b1a" stroke-width="1.1"/></svg>
      www.quelvatrix-moor.com
    </li>
  </ul>
</section>

<section class="card card--back" aria-label="Card back">
  <div class="back__rule"></div>

  <div class="back__copy">
    <p class="back__heading">What does your dream house have</p>
    <p>swimming pool x<br>private vineyard x<br>herb garden x<br>full sized football pitch x</p>

    <p class="back__heading back__heading--gap">How to buy a home abroad:</p>
    <p class="back__muted">Method 1:</p>
    <p>1) Scour internet for suitable estate agents<br>
       2) Arrange hectic holiday timetable with multiple agents in multiple languages<br>
       3) Fly to destination to find property was not as it seemed<br>
       4) Feel frustrated and helpless</p>
    <p class="back__muted">OR<br>Method 2:</p>
    <p>Contact your expert home hunter (details overleaf) - and leave the hard work to them</p>
  </div>

  <div class="brand back__brand">
    <span class="brand__dot"></span>
    <span class="back__brand-name">Quelvatrix Moor</span>
    <span class="back__brand-sub">FARAWAY NEST FINDERS</span>
  </div>
</section>

</body>
</html>
```